Contemporary Elegant Business Card Design for an International Trade Company in the Wine Industry

We need a new business card design for an international trade company in the wine and winemaking industry. The overall feel of the card should be contemporary, upscale, luxurious and elegant. It should communicate confidence and professionalism. The colors should complementary to our logo design (burgundy, gold, and black).
Inspiration: rich velvet tapestry
The card should include the following information:
Business: Corvelle Trading/Shipping, LLC.
Name: Martin R. Obrastow
Title: CEO
Email: marty@corvelletrading.example
Phone: 555-482-1957
www.corvelletrading.example
Reason: We'd like the designers that we requested some additional designs from to still submit designs. Thank you!
Business
Contact Information for Business Card
Title: CEO
Phone: 555-482-1957
www.corvelletrading.example

```html
<!DOCTYPE html>
<html lang="en">
<head>
<meta charset="utf-8">
<title>Corvelle Trading/Shipping – Business Card</title>
<link rel="stylesheet" href="https://fonts.googleapis.com/css2?family=Signika:wght@400;500;600&display=swap">
<style>
  :root {
    --page-bg: #e7e3de;
    --card-bg: #f7f4f0;
    --burgundy: #7e1f2b;
    --burgundy-deep: #6a1823;
    --gold: #c9962f;
    --charcoal: #4a4646;
    --ink: #2b2323;
    --name-tint: #f2ddd6;
    --white: #ffffff;
  }
  * { margin: 0; padding: 0; box-sizing: border-box; }
  html, body {
    width: 1200px;
    height: 1032px;
    overflow: hidden;
    background: var(--page-bg);
    font-family: "Signika", "Trebuchet MS", sans-serif;
  }
  .card {
    position: absolute;
    left: 100px;
    top: 220px;
    width: 1000px;
    height: 592px;
    background: var(--card-bg);
    box-shadow: 0 10px 30px rgba(0,0,0,0.12);
    overflow: hidden;
  }
  .card-waves {
    position: absolute;
    inset: 0;
    width: 100%;
    height: 100%;
  }
  .holder-name {
    position: absolute;
    right: 66px;
    top: 66px;
    font-size: 33px;
    font-weight: 500;
    color: var(--name-tint);
    letter-spacing: 0.2px;
  }
  .holder-title {
    position: absolute;
    right: 66px;
    top: 124px;
    font-size: 19px;
    font-weight: 400;
    color: var(--white);
  }
  .brand-mark {
    position: absolute;
    left: 90px;
    top: 162px;
    width: 290px;
    height: 290px;
    background: var(--burgundy);
  }
  .brand-name {
    position: absolute;
    left: 90px;
    top: 454px;
    width: 290px;
    text-align: center;
    font-size: 52px;
    font-weight: 600;
    line-height: 1;
    color: var(--ink);
    letter-spacing: 1px;
  }
  .contact-list {
    position: absolute;
    right: 73px;
    top: 410px;
    list-style: none;
  }
  .contact-item {
    display: flex;
    justify-content: flex-end;
    align-items: center;
    gap: 18px;
    height: 37px;
    font-size: 24px;
    color: var(--ink);
  }
  .contact-icon {
    width: 20px;
    height: 20px;
    flex: none;
  }
</style>
</head>
<body>
  <main class="card">
    <svg class="card-waves" viewBox="0 0 802 475" preserveAspectRatio="none" aria-hidden="true">
      <path d="M0,0 H802 V212 C650,205 560,140 450,90 C350,45 200,25 0,30 Z" fill="var(--burgundy)"/>
      <path d="M0,55 C120,25 330,30 445,85 C330,50 150,55 0,100 Z" fill="var(--charcoal)"/>
      <path d="M70,85 C250,60 380,80 500,140 C620,200 700,232 802,238 L802,246 C690,240 610,210 490,150 C380,95 250,72 70,85 Z" fill="var(--gold)"/>
    </svg>

    <h1 class="holder-name">Martin R. Obrastow</h1>
    <p class="holder-title">CEO</p>

    <div class="brand-mark" aria-hidden="true"></div>
    <p class="brand-name">CORVELLE</p>

    <ul class="contact-list">
      <li class="contact-item">
        <span>555-482-1957</span>
        <svg class="contact-icon" viewBox="0 0 20 20" aria-hidden="true">
          <rect x="3" y="9" width="14" height="9" rx="2" fill="var(--gold)"/>
          <path d="M1,8 C1,3 19,3 19,8 L15,9 L14,6 H6 L5,9 Z" fill="var(--gold)"/>
          <circle cx="10" cy="13.5" r="2" fill="var(--card-bg)"/>
        </svg>
      </li>
      <li class="contact-item">
        <span>marty@corvelletrading.example</span>
        <svg class="contact-icon" viewBox="0 0 20 20" aria-hidden="true">
          <rect x="1" y="4" width="18" height="12" fill="var(--gold)"/>
          <path d="M1,4 L10,11 L19,4" fill="none" stroke="var(--card-bg)" stroke-width="1.4"/>
        </svg>
      </li>
      <li class="contact-item">
        <span>www.corvelletrading.example</span>
        <svg class="contact-icon" viewBox="0 0 20 20" aria-hidden="true">
          <circle cx="10" cy="10" r="8.5" fill="var(--gold)"/>
          <g fill="none" stroke="var(--card-bg)" stroke-width="1">
            <ellipse cx="10" cy="10" rx="3.8" ry="8.5"/>
            <line x1="1.5" y1="10" x2="18.5" y2="10"/>
            <line x1="10" y1="1.5" x2="10" y2="18.5"/>
          </g>
        </svg>
      </li>
    </ul>
  </main>
</body>
</html>
```